General contractor/GM consaltant business card

I need a card for my contracting company in North Dakota, we build industrial buildings for the oil feild and oil feild related companies offices, shops, airplain hangars, airports ext. We have a familly atmosphere on the job and are very relational and personal.
Industry/Entity Type
Industrial
Contact Information for Business Card
Hollowpine Crafters LLC.
Dale T.Voskuijl
4873 Quenwick dr. Colorado Springs, CO. 80462
Cell# 406-738-1452
dale@hollowpinecrafters.example

```html
<!DOCTYPE html>
<html lang="en">
<head>
<meta charset="utf-8">
<title>Hollowpine Crafters LLC. — Business Card</title>
<link rel="stylesheet" href="https://fonts.googleapis.com/css2?family=Arimo:wght@400&family=Philosopher:wght@700&display=swap">
<style>
  :root {
    --page-bg: #e4e2de;
    --card-bg: #ffffff;
    --brand-red: #d3212d;
    --brand-blue: #2a5ca8;
    --text-slate: #3d5a8a;
    --gap-white: #ffffff;
  }
  * { box-sizing: border-box; margin: 0; padding: 0; }
  html, body {
    width: 1200px;
    height: 858px;
    overflow: hidden;
    background: var(--page-bg);
  }
  .canvas { position: relative; width: 1200px; height: 858px; }

  .card {
    position: absolute;
    left: 285px;
    width: 630px;
    height: 360px;
    background: var(--card-bg);
    box-shadow: 0 5px 18px rgba(0,0,0,0.18);
    overflow: hidden;
    font-family: "Arimo", Arial, sans-serif;
  }
  .card-front { top: 40px; }
  .card-back  { top: 458px; }

  .brand { position: absolute; display: flex; align-items: center; gap: 12px; }
  .brand-mark {
    width: 22px; height: 22px; border-radius: 50%;
    background: var(--brand-blue); flex: none;
  }
  .brand-name {
    font-family: "Philosopher", Georgia, serif;
    font-weight: 700;
    color: var(--brand-red);
    white-space: nowrap;
  }
  .card-front .brand { left: 40px; top: 104px; }
  .card-front .brand-name { font-size: 30px; }

  .card-back .brand {
    left: 0; right: 0; top: 118px;
    justify-content: center;
  }
  .card-back .brand-name { font-size: 36px; }

  .person-name {
    position: absolute;
    left: 380px;
    top: 52px;
    font-size: 19px;
    color: var(--brand-red);
    white-space: nowrap;
  }

  .contact-list { position: absolute; left: 46px; top: 178px; list-style: none; }
  .contact-item {
    display: flex; align-items: center; gap: 12px;
    height: 27px;
    font-size: 14px;
    color: var(--text-slate);
    white-space: nowrap;
  }
  .contact-icon { width: 15px; height: 15px; fill: var(--brand-red); flex: none; }

  .stripe { position: absolute; left: 0; width: 100%; }
  .stripe-blue { top: 284px; height: 32px; background: var(--brand-blue); }
  .stripe-gap  { top: 316px; height: 8px;  background: var(--gap-white); }
  .stripe-red  { top: 324px; height: 36px; background: var(--brand-red); }
</style>
</head>
<body>
<div class="canvas">
  <section class="card card-front">
    <div class="brand">
      <span class="brand-mark"></span>
      <span class="brand-name">Hollowpine Crafters LLC.</span>
    </div>

    <p class="person-name">Dale T.Voskuijl</p>

    <ul class="contact-list">
      <li class="contact-item">
        <svg class="contact-icon" viewBox="0 0 24 24" aria-hidden="true">
          <path d="M6.6 10.8a15.1 15.1 0 0 0 6.6 6.6l2.2-2.2a1 1 0 0 1 1-.25 11.4 11.4 0 0 0 3.6.57 1 1 0 0 1 1 1V20a1 1 0 0 1-1 1A17 17 0 0 1 3 4a1 1 0 0 1 1-1h3.5a1 1 0 0 1 1 1c0 1.25.2 2.45.57 3.6a1 1 0 0 1-.25 1z"/>
        </svg>
        <span>406-738-1452</span>
      </li>
      <li class="contact-item">
        <svg class="contact-icon" viewBox="0 0 24 24" aria-hidden="true">
          <path d="M12 2a7 7 0 0 0-7 7c0 5.2 7 13 7 13s7-7.8 7-13a7 7 0 0 0-7-7zm0 9.5A2.5 2.5 0 1 1 12 6.5a2.5 2.5 0 0 1 0 5z"/>
        </svg>
        <span>4873 Quenwick dr. Colorado Springs, CO. 80462</span>
      </li>
      <li class="contact-item">
        <svg class="contact-icon" viewBox="0 0 24 24" aria-hidden="true">
          <path d="M2 5h20v14H2z M4 7v.4l8 5.2 8-5.2V7l-8 5.2z" fill-rule="evenodd"/>
        </svg>
        <span>dale@hollowpinecrafters.example</span>
      </li>
    </ul>

    <div class="stripe stripe-blue"></div>
    <div class="stripe stripe-gap"></div>
    <div class="stripe stripe-red"></div>
  </section>

  <section class="card card-back">
    <div class="brand">
      <span class="brand-mark"></span>
      <span class="brand-name">Hollowpine Crafters LLC.</span>
    </div>

    <div class="stripe stripe-blue"></div>
    <div class="stripe stripe-gap"></div>
    <div class="stripe stripe-red"></div>
  </section>
</div>
</body>
</html>
```